Legal Stationary

A full set of stationery is required
The image and logo, along with colour, are set and attached.
The style should be modern, clean, and corporate. Not just a basic template off the web.
In addition to the address/website/email/phone fields for DX and KWT number, with the text “the firm is authorised and regulated by the KWT”
All files in all formats will be needed to allow editing after. Initial setup of templates will be required, and details for 4 business cards will be supplied.
Target Market(s)
Consumers of legal services
Industry/Entity Type
Legal

```html
<!DOCTYPE html>
<html lang="en">
<head>
<meta charset="utf-8">
<title>Marlow Legal – Business Card</title>
<link rel="stylesheet" href="https://fonts.googleapis.com/css2?family=Arimo:wght@400;700&display=swap">
<style>
  :root {
    --backdrop: #1b1b1d;
    --card: #f7f7f5;
    --brand-blue: #1e2e8f;
    --ink: #3a3a3a;
    --charcoal: #2c2c2c;
    --white: #ffffff;
  }
  * { margin: 0; padding: 0; box-sizing: border-box; }
  html, body {
    width: 1200px; height: 963px; overflow: hidden;
    background: var(--backdrop);
    font-family: "Arimo", Arial, sans-serif;
  }
  .business-card {
    position: absolute;
    left: 100px; top: 196px;
    width: 1000px; height: 571px;
    background: var(--card);
    box-shadow: 0 20px 50px rgba(0,0,0,0.5);
    overflow: hidden;
  }
  .name-band {
    position: absolute;
    left: 0; top: 36px;
    width: 600px; height: 82px;
    background: var(--brand-blue);
    color: var(--white);
    padding: 14px 0 0 56px;
  }
  .holder-name {
    font-weight: 700;
    font-size: 27px;
    letter-spacing: 0.5px;
    text-transform: uppercase;
    line-height: 1;
  }
  .holder-role {
    font-size: 21px;
    font-weight: 400;
    margin-top: 4px;
    margin-left: -20px;
  }
  .firm-name {
    position: absolute;
    left: 624px; top: 66px;
    width: 316px;
    font-weight: 700;
    font-size: 37px;
    line-height: 1;
    color: var(--brand-blue);
    letter-spacing: 0.5px;
    white-space: nowrap;
  }
  .accent-square {
    position: absolute;
    right: 0; top: 118px;
    width: 46px; height: 46px;
    background: var(--charcoal);
  }
  .contact-list {
    position: absolute;
    left: 46px; top: 300px;
    list-style: none;
    color: var(--ink);
    font-size: 22px;
  }
  .contact-item {
    display: flex; align-items: center;
    gap: 10px;
    height: 32px;
  }
  .contact-icon { width: 20px; height: 20px; flex: none; }
  .office-address {
    position: absolute;
    right: 250px; top: 452px;
    text-align: right;
    color: var(--ink);
    font-size: 22px;
    line-height: 1.25;
    font-style: normal;
  }
</style>
</head>
<body>
  <article class="business-card">
    <header class="name-band">
      <h1 class="holder-name">Daniel Harper</h1>
      <p class="holder-role">Manager</p>
    </header>

    <div class="firm-name">MARLOW LEGAL</div>
    <div class="accent-square"></div>

    <ul class="contact-list">
      <li class="contact-item">
        <svg class="contact-icon" viewBox="0 0 20 20" aria-hidden="true">
          <circle cx="10" cy="10" r="10" fill="#1e2e8f"/>
          <path d="M6.5 5.5c.6-.5 1.3-.4 1.6.1l1 1.6c.3.5.1 1-.3 1.3l-.6.4c.6 1.3 1.6 2.3 2.9 2.9l.4-.6c.3-.4.8-.6 1.3-.3l1.6 1c.5.3.6 1 .1 1.6-.8.9-2 1.2-3.1.7-2.7-1.1-4.5-2.9-5.6-5.6-.5-1.1-.2-2.3.7-3.1z" fill="#fff"/>
        </svg>
        <span>123-456-2100</span>
      </li>
      <li class="contact-item">
        <svg class="contact-icon" viewBox="0 0 20 20" aria-hidden="true">
          <circle cx="10" cy="10" r="10" fill="#1e2e8f"/>
          <rect x="4.5" y="6.5" width="11" height="7.5" fill="none" stroke="#fff" stroke-width="1.4"/>
          <path d="M4.5 6.5l5.5 4.3 5.5-4.3" fill="none" stroke="#fff" stroke-width="1.4"/>
        </svg>
        <span>youremail@mailbox.com</span>
      </li>
      <li class="contact-item">
        <svg class="contact-icon" viewBox="0 0 20 20" aria-hidden="true">
          <circle cx="10" cy="10" r="10" fill="#1e2e8f"/>
          <circle cx="10" cy="10" r="5.5" fill="none" stroke="#fff" stroke-width="1.3"/>
          <ellipse cx="10" cy="10" rx="2.3" ry="5.5" fill="none" stroke="#fff" stroke-width="1.1"/>
          <path d="M4.5 10h11" stroke="#fff" stroke-width="1.1"/>
        </svg>
        <span>www.yourwebsite.com</span>
      </li>
    </ul>

    <address class="office-address">
      Your Address, City<br>State, Zip 0000
    </address>
  </article>
</body>
</html>
```